A Speech Therapy Business needs to update their logo

I need an update to the font and color of my logo to look more appealing. I am looking to open a private practice as a Speech Language Pathologist that caters to adults and children. It needs to be sophisticated and friendly at the same time. I want to keep the silhouette in my logo as is, just update the font and color for "Brightpaths".
Industry/Entity Type
Business
Contact Information for Business Card
I want the business card to have my logo, my name (Dorota Valk, CCC-SLP, TSSLD) and that I am a Bilingual Speech Language Pathologist. Also, include my phone number, (555) 271-8390. Include my website, Brightpathsslp.example, and email address, dorotavalk@brightpathsslp.example
Look and feel
Each slider illustrates characteristics of the customer's brand and the style your logo design should communicate.

```html
<!DOCTYPE html>
<html lang="en">
<head>
<meta charset="utf-8">
<title>Brightpaths – Business Card</title>
<link rel="stylesheet" href="https://fonts.googleapis.com/css2?family=Lato:wght@400;700;900&display=swap">
<style>
  :root {
    --backdrop: #ecebe8;
    --card: #fbfbfb;
    --brand-blue: #29aedb;
    --brand-blue-deep: #1f93c4;
    --ink: #1d1d1f;
    --silhouette: #222427;
    --rule: #b9b3d6;
    --band-edge: #1a1a1a;
  }
  * { box-sizing: border-box; margin: 0; padding: 0; }
  html, body { width: 1200px; height: 780px; overflow: hidden; }
  body {
    background: var(--backdrop);
    font-family: "Lato", Arial, sans-serif;
    color: var(--ink);
    position: relative;
  }
  .card {
    position: absolute;
    top: 75px;
    width: 360px;
    height: 630px;
    background: var(--card);
    border-radius: 22px;
    overflow: hidden;
    box-shadow: 0 10px 30px rgba(0,0,0,0.18);
  }
  .card--front { left: 200px; }
  .card--back { left: 640px; }

  .logo { display: flex; flex-direction: column; align-items: center; }
  .logo__figures {
    width: 270px;
    height: 62px;
    background: linear-gradient(90deg, var(--silhouette), #3a3d42);
    border-radius: 6px;
  }
  .logo__name {
    margin-top: 6px;
    font-weight: 900;
    font-size: 44px;
    letter-spacing: 1px;
    text-transform: uppercase;
    color: var(--brand-blue);
    line-height: 1;
  }

  .card--front .logo { margin-top: 58px; }
  .person { margin: 52px 34px 0; }
  .person__name {
    font-size: 24px;
    font-weight: 400;
    color: var(--brand-blue);
    letter-spacing: 1px;
    text-transform: uppercase;
  }
  .person__credentials { font-size: 16px; }
  .person__title { margin-top: 4px; font-size: 15.5px; color: var(--ink); }

  .contact { margin: 42px 34px 0; }
  .contact__rule {
    height: 1px;
    background: linear-gradient(90deg, #8f8fb8, var(--rule) 60%, transparent);
    margin-bottom: 16px;
  }
  .contact__label { font-size: 14px; color: var(--brand-blue); }
  .contact__value { font-size: 22px; margin-bottom: 14px; }
  .contact__value--email { font-size: 16.5px; }

  .band {
    position: absolute;
    left: 0; right: 0;
    height: 82px;
    background: linear-gradient(180deg, var(--brand-blue), var(--brand-blue-deep));
    display: flex; align-items: center; justify-content: center;
    color: #fff;
    font-size: 20px;
    letter-spacing: 0.5px;
  }
  .card--front .band { bottom: 0; border-top: 2px solid var(--band-edge); }
  .card--back .band { top: 0; border-bottom: 2px solid var(--band-edge); }

  .card--back .logo { margin-top: 220px; }
  .card--back .logo__figures { width: 290px; height: 70px; }
</style>
</head>
<body>
  <article class="card card--front">
    <div class="logo">
      <div class="logo__figures" role="img" aria-label="Silhouettes of an adult and children walking hand in hand"></div>
      <div class="logo__name">Brightpaths</div>
    </div>
    <div class="person">
      <p class="person__name">Dorota Valk,<span class="person__credentials"> CCC-SLP, TSSLD</span></p>
      <p class="person__title">Bilingual Speech Language Pathologist</p>
    </div>
    <div class="contact">
      <div class="contact__rule"></div>
      <p class="contact__label">Phone</p>
      <p class="contact__value">(555) 271-8390</p>
      <p class="contact__label">Email</p>
      <p class="contact__value contact__value--email">dorotavalk@brightpathsslp.example</p>
    </div>
    <div class="band">www.Brightpathsslp.example</div>
  </article>

  <article class="card card--back">
    <div class="band">brightpathsslp.example</div>
    <div class="logo">
      <div class="logo__figures" role="img" aria-label="Silhouettes of an adult and children walking hand in hand"></div>
      <div class="logo__name">Brightpaths</div>
    </div>
  </article>
</body>
</html>
```